Driving School Business card design

Hi, we are starting a new business (Driving School) and would like your help with our business card design.
We are located in Adelaide SA.
Our aim is to help young people achieve best possible results by promoting safe and stress free driving.

Name of our school is "Brindle" which means best or most favorable.

Hope there is someone out there in wonderful world of design who can think outside of square and give us recognizable/ unique business card design.

Target Market(s)

16+

Industry/Entity Type

Business

Contact Information for Business Card

Name of our business is "Brindle driver training"
Our idea is to make letter "L' in Brindle more distinct (noticeable) by different color or font, so it gets associated with learner driver.
We like combination of white, dark gray and yellow but do not limit our self to that.
Reverse side of our card would have to incorporate writing space for date and time of the next lesson.

Requirements
Must have
• Business name: Brindle driver training
• Owner/ instructor name
• Mobile no:
• Loopnest logo
Should not have
• Anything Not associated with driving

```html
<!DOCTYPE html>
<html lang="en">
<head>
<meta charset="utf-8">
<title>Brindle driver training – business card</title>
<link rel="stylesheet" href="https://fonts.googleapis.com/css2?family=Montserrat:wght@600&family=Open+Sans:wght@400;600;700&display=swap">
<style>
  :root {
    --bg: #9a9a9a;
    --card-white: #f4f4f4;
    --card-white-shade: #d9d9d9;
    --ink-dark: #1c1c1c;
    --band-dark: #141414;
    --band-edge: #6a6a6a;
    --road-grey: #5a5a5a;
    --text-grey: #555555;
    --rule-grey: #8c8c8c;
    --accent-yellow: #e4e33a;
    --light-text: #f2f2f2;
  }
  * { box-sizing: border-box; margin: 0; padding: 0; }
  html, body { width: 1200px; height: 900px; overflow: hidden; }
  body {
    background: radial-gradient(ellipse at center, #c4c4c4 0%, var(--bg) 70%, #8a8a8a 100%);
    font-family: "Open Sans", Arial, sans-serif;
    position: relative;
  }
  .card {
    position: absolute;
    width: 540px;
    height: 320px;
    border-radius: 18px;
    overflow: hidden;
    box-shadow: 0 8px 22px rgba(0,0,0,0.35);
  }
  .card-front { left: 50px; top: 130px; }
  .card-back { left: 610px; top: 450px; }
  .card svg.card-art { position: absolute; inset: 0; width: 540px; height: 320px; }

  .brand {
    position: absolute;
    display: flex;
    align-items: center;
    gap: 10px;
    font-family: "Open Sans", Arial, sans-serif;
    font-weight: 600;
    font-size: 27px;
    letter-spacing: -0.3px;
    white-space: nowrap;
  }
  .brand-mark { width: 18px; height: 18px; background: var(--accent-yellow); }
  .card-front .brand { left: 40px; top: 34px; color: var(--text-grey); }
  .card-back .brand { right: 28px; top: 20px; color: #d4d4d4; font-size: 22px; gap: 8px; }
  .card-back .brand-mark { width: 15px; height: 15px; }

  .holder-name {
    position: absolute; left: 40px; top: 118px;
    font-family: "Montserrat", Arial, sans-serif; font-weight: 600;
    font-size: 22px; color: var(--ink-dark);
  }
  .holder-role {
    position: absolute; left: 41px; top: 148px;
    font-size: 12px; color: var(--text-grey);
  }
  .contact-list {
    position: absolute; left: 40px; top: 192px;
    list-style: none; color: var(--light-text); font-size: 13px; line-height: 19px;
  }
  .contact-list li { display: flex; align-items: center; gap: 6px; }
  .contact-list svg { width: 12px; height: 12px; flex: none; }
  .address {
    position: absolute; left: 40px; top: 262px;
    color: var(--light-text); font-size: 13px; line-height: 18px; font-style: normal;
  }
  .address strong { font-weight: 700; }

  .field-label {
    position: absolute; font-size: 13px; letter-spacing: 0.5px; color: var(--ink-dark);
  }
  .write-line {
    position: absolute; height: 1px; background: var(--rule-grey);
  }
</style>
</head>
<body>

<section class="card card-front" aria-label="Card front">
  <svg class="card-art" viewBox="0 0 540 320">
    <defs>
      <linearGradient id="frontWhite" x1="0" y1="0" x2="1" y2="0">
        <stop offset="0" stop-color="#ffffff"/>
        <stop offset="1" stop-color="#d6d6d6"/>
      </linearGradient>
      <linearGradient id="frontBand" x1="0" y1="0" x2="1" y2="0">
        <stop offset="0" stop-color="#2a2a2a"/>
        <stop offset="1" stop-color="#101010"/>
      </linearGradient>
      <linearGradient id="roadArea" x1="0" y1="1" x2="1" y2="0">
        <stop offset="0" stop-color="#5c5c5c"/>
        <stop offset="1" stop-color="#2c2c2c"/>
      </linearGradient>
    </defs>
    <rect width="540" height="320" fill="url(#frontWhite)"/>
    <path d="M0,178 L320,178 C420,178 440,80 540,55 L540,320 L0,320 Z" fill="url(#frontBand)"/>
    <path role="img" aria-label="Winding road illustration" d="M330,320 C340,230 420,200 440,150 C455,110 470,80 540,62 L540,320 Z" fill="url(#roadArea)"/>
  </svg>

  <div class="brand"><span class="brand-mark"></span>Brindle driver training</div>
  <div class="holder-name">Marcus Hale</div>
  <div class="holder-role">Director</div>

  <ul class="contact-list">
    <li>
      <svg viewBox="0 0 12 12"><path d="M1,4 C3,1 9,1 11,4 L9,5 L8,3.5 L4,3.5 L3,5 Z M2.5,6 L9.5,6 L10.5,10.5 L1.5,10.5 Z" fill="var(--accent-yellow)"/></svg>
      0412 555 019
    </li>
    <li>
      <svg viewBox="0 0 12 12"><rect x="0.5" y="2" width="11" height="8" fill="var(--accent-yellow)"/><path d="M0.5,2 L6,7 L11.5,2" fill="none" stroke="#1c1c1c" stroke-width="1"/></svg>
      marcus@brindledriving.com.au
    </li>
    <li>
      <svg viewBox="0 0 12 12"><circle cx="6" cy="6" r="5.5" fill="var(--accent-yellow)"/><path d="M0.5,6 H11.5 M6,0.5 V11.5 M3,2 C4.5,4 4.5,8 3,10 M9,2 C7.5,4 7.5,8 9,10" fill="none" stroke="#1c1c1c" stroke-width="0.7"/></svg>
      www.brindledriving.com.au
    </li>
  </ul>

  <address class="address">
    <strong>Company name</strong><br>
    42 Kestrel Lane<br>
    Norwood SA 5067
  </address>
</section>

<section class="card card-back" aria-label="Card back">
  <svg class="card-art" viewBox="0 0 540 320">
    <defs>
      <linearGradient id="backWhite" x1="0" y1="0" x2="1" y2="1">
        <stop offset="0" stop-color="#ffffff"/>
        <stop offset="1" stop-color="#e2e2e2"/>
      </linearGradient>
    </defs>
    <rect width="540" height="320" fill="url(#backWhite)"/>
    <path d="M100,0 C170,40 250,75 330,84 C400,100 470,150 540,185" fill="none" stroke="var(--band-edge)" stroke-width="10"/>
    <path d="M100,0 L540,0 L540,180 C470,145 400,96 330,80 C250,70 170,38 100,0 Z" fill="var(--band-dark)"/>
  </svg>

  <div class="brand"><span class="brand-mark"></span>Brindle driver training</div>

  <span class="field-label" style="left:58px; top:36px;">DATE</span>
  <span class="field-label" style="left:196px; top:70px;">TIME</span>
  <div class="write-line" style="left:40px; top:82px; width:140px;"></div>
  <div class="write-line" style="left:190px; top:100px; width:110px;"></div>
  <div class="write-line" style="left:40px; top:124px; width:140px;"></div>
  <div class="write-line" style="left:190px; top:140px; width:110px;"></div>
  <div class="write-line" style="left:40px; top:166px; width:140px;"></div>
  <div class="write-line" style="left:190px; top:180px; width:110px;"></div>
  <div class="write-line" style="left:40px; top:208px; width:140px;"></div>
  <div class="write-line" style="left:190px; top:222px; width:110px;"></div>
  <div class="write-line" style="left:40px; top:250px; width:140px;"></div>
  <div class="write-line" style="left:190px; top:264px; width:110px;"></div>

  <span class="field-label" style="left:340px; top:152px;">DATE</span>
  <span class="field-label" style="left:470px; top:186px;">TIME</span>
  <div class="write-line" style="left:320px; top:194px; width:130px;"></div>
  <div class="write-line" style="left:462px; top:208px; width:60px;"></div>
  <div class="write-line" style="left:320px; top:230px; width:130px;"></div>
  <div class="write-line" style="left:462px; top:244px; width:60px;"></div>
  <div class="write-line" style="left:320px; top:266px; width:130px;"></div>
  <div class="write-line" style="left:462px; top:280px; width:60px;"></div>
  <div class="write-line" style="left:320px; top:300px; width:130px;"></div>
</section>

</body>
</html>
```